Simple Business Cards for Self-employed Coach

Simple business card with a design that includes the QLT logo.
Using either only the logo color or additional colors that match the logo.

Meridian Guides reach deeply into the past, gathering wisdom from East and West, while still staying current with the frontiers of new discovery in cognitive science, genetics, and other disciplines. see https://www.brightharborpath.example/what-is-integral-coaching/

Target Market(s)

Coaching Clients in Tokyo /Asia; in business organizations, but also outside

Industry/Entity Type

Life Coaching

Contact Information for Business Card

Lukas Brenning
Certified Meridian Guide

3-2-48 Kamiyoshi
Nakarino 164-0392
Tokyo, Japan

Phone: +81 70 4817 5062
E-Mail: lukas.brenning@mailora.example

Font styles to use
Sans Serif

Colors
00a990

Requirements
Must have
• include uploaded logo
• color fitting with QLT logo color
Nice to have
• simple, elegant design
Should not have
• clutter

```html
<!DOCTYPE html>
<html lang="en">
<head>
<meta charset="utf-8">
<title>Lukas Brenning – Business Card</title>
<link href="https://fonts.googleapis.com/css2?family=Open+Sans:wght@400;600&display=swap" rel="stylesheet">
<style>
  :root {
    --teal: #1f8f86;
    --teal-bright: #00a990;
    --card: #ffffff;
    --backdrop: #e9ecec;
  }
  html, body {
    margin: 0;
    width: 1200px;
    height: 902px;
    overflow: hidden;
    background: var(--backdrop);
    font-family: "Open Sans", sans-serif;
  }
  .business-card {
    position: absolute;
    left: 75px;
    top: 151px;
    width: 1050px;
    height: 600px;
    background: var(--card);
    box-shadow: 0 6px 24px rgba(0,0,0,.15);
    overflow: hidden;
    color: var(--teal);
  }
  .brand {
    position: absolute;
    right: 70px;
    top: 60px;
    display: flex;
    align-items: center;
    gap: 16px;
  }
  .brand-square {
    width: 44px;
    height: 44px;
    background: var(--teal);
  }
  .brand-name {
    font-size: 52px;
    font-weight: 600;
    letter-spacing: 10px;
    color: var(--teal);
    line-height: 1;
  }
  .identity {
    position: absolute;
    left: 360px;
    top: 245px;
  }
  .person-name {
    font-size: 56px;
    font-weight: 600;
    letter-spacing: 2px;
    margin: 0;
    line-height: 1.1;
    padding-bottom: 4px;
    border-bottom: 3px solid var(--teal);
  }
  .person-title {
    font-size: 32px;
    font-weight: 400;
    margin: 6px 0 0;
  }
  .contact-band {
    position: absolute;
    left: 0;
    top: 390px;
    width: 100%;
    height: 112px;
    background: var(--teal);
    color: #fff;
  }
  .contact-line {
    position: absolute;
    display: flex;
    align-items: center;
    gap: 22px;
    font-size: 26px;
    letter-spacing: 1px;
  }
  .contact-line.phone { left: 300px; top: 10px; }
  .contact-line.email { left: 230px; top: 56px; }
  .contact-line svg { width: 26px; height: 26px; }
  .divider {
    position: absolute;
    left: 150px;
    top: 514px;
    width: 520px;
    display: flex;
    align-items: center;
    gap: 16px;
  }
  .divider .rule { flex: 1; height: 4px; background: var(--teal); }
  .divider svg { width: 26px; height: 26px; }
  .address {
    position: absolute;
    left: 36px;
    top: 548px;
    font-size: 27px;
    margin: 0;
    font-style: normal;
  }
</style>
</head>
<body>
  <div class="business-card">
    <div class="brand">
      <div class="brand-square"></div>
      <div class="brand-name">QLT</div>
    </div>

    <div class="identity">
      <h1 class="person-name">Lukas Brenning</h1>
      <p class="person-title">Certified Meridian Guide</p>
    </div>

    <div class="contact-band">
      <div class="contact-line phone">
        <svg viewBox="0 0 24 24" aria-hidden="true"><path fill="#fff" d="M6.6 10.8a15 15 0 0 0 6.6 6.6l2.2-2.2a1 1 0 0 1 1-.25 11.4 11.4 0 0 0 3.6.57 1 1 0 0 1 1 1V20a1 1 0 0 1-1 1A17 17 0 0 1 3 4a1 1 0 0 1 1-1h3.5a1 1 0 0 1 1 1c0 1.25.2 2.45.57 3.57a1 1 0 0 1-.25 1z"/></svg>
        <span>+81 70 4817 5062</span>
      </div>
      <div class="contact-line email">
        <svg viewBox="0 0 24 24" aria-hidden="true"><rect x="2" y="5" width="20" height="14" fill="#fff"/><path d="M2 5l10 8 10-8M2 19l7-7M22 19l-7-7" stroke="var(--teal)" stroke-width="1.6" fill="none"/></svg>
        <span>lukas.brenning@mailora.example</span>
      </div>
    </div>

    <div class="divider">
      <div class="rule"></div>
      <svg viewBox="0 0 24 24" aria-hidden="true"><path fill="var(--teal)" d="M12 3l10 9h-3v9h-5v-6h-4v6H5v-9H2z"/></svg>
      <div class="rule"></div>
    </div>

    <address class="address">3-2-48 Kamiyoshi, Nakarino 164-0392, Tokyo, Japan</address>
  </div>
</body>
</html>
```